Design a Website in Wordpress for an Australian Health Training Company in Health related courses

We require a WORDPRESS based Website (due to add on's we need to use for third party software) to replace our old site.
We offer national face to face delivery in medical reception, terminology and also administration.
The website will have around 6 pages and the ability to describe our main 6 courses (perhaps on the Courses page this may be tabs opening up to details for example?)
I have attached a previous sample of a Joomla site which was being developed (please do not feel you have to copy this - but I am just giving it as a sample - copying would be boring). But it gives an idea of look/feel and colours which may be suitable. Open to other ideas though.
I will provide some of the content, but would like the ability to finish the content myself.
Images and graphics are important. While a few medical photos re great - don't be tempted to us all pictures of doctors and nurses (although a couple would be good) - these are administrative courses so general corporate, eye catching visionary pictures of people in general are great. A medical type picture is also fine.
THE BOOKING system - will be via an ADD ON which will occur at the end of the project and is supplied by a third party software company (our student management system). This project will include up to 2 hours working with the Tech guys from the third party software to enable the ADD ON. If this ADD ON requires more time, we will pay hourly (although I do not expect it will).
Mostly a female market, many mature aged women target 25-45 yrs. Mixture of medical/health and corporate. Maybe a bit of mums returning to work and corporate inspiration.
Must have
- Wordpress
- Great graphics
- Interesting
- professional and clean
- Enquiry section (info Pak)
- Should have a University feel to it - Education
- Pages
- Home Page - About Us - Recruitment -Courses - Class Schedule - Traineeships Queensland Funding - Latest News Blog - Corporate Training- Contact us

```html
<!DOCTYPE html>
<html lang="en">
<head>
<meta charset="utf-8">
<title>Wellmere Institute of Training</title>
<link href="https://fonts.googleapis.com/css2?family=Cinzel:wght@400;700&family=Open+Sans:wght@400;600;700&display=swap" rel="stylesheet">
<style>
:root{
  --navy:#1c3d78;
  --blue:#1f56a8;
  --orange:#f39a1e;
  --ink:#333;
  --muted:#777;
  --grey:#efefef;
  --dark:#1c1c1c;
  --line:#dcdcdc;
}
*{box-sizing:border-box;margin:0;padding:0}
html,body{width:1200px;height:5070px;overflow:hidden}
body{font-family:"Open Sans",Arial,sans-serif;color:var(--ink);font-size:13px;background:#fff;position:relative}
.btn{display:inline-block;background:var(--orange);color:#fff;font-size:12px;font-weight:600;padding:7px 18px;border-radius:2px}
.ph{display:block}
.sec-head{text-align:center}
.sec-head .crest{width:30px;height:30px;border:2px solid var(--navy);margin:0 auto 14px}
.sec-head h2{font-family:"Cinzel",Georgia,serif;font-size:28px;font-weight:400;color:#222;letter-spacing:1px}
.sec-head h2 span{color:var(--blue)}
.sec-head .rule{width:60px;height:2px;background:var(--orange);margin:10px auto 0}

/* header */
.topbar{height:118px;position:relative;border-bottom:1px solid var(--line)}
.brand{position:absolute;left:95px;top:20px;display:flex;align-items:center;gap:10px}
.brand .mark{width:40px;height:40px;background:var(--navy);flex:none}
.brand .name{font-weight:700;color:var(--navy);font-size:14px;line-height:1.25;width:140px}
.socials{position:absolute;left:320px;top:12px;display:flex;gap:6px}
.socials i{width:20px;height:20px;border-radius:50%;background:var(--navy);display:block}
.tools{position:absolute;right:95px;top:12px;display:flex;gap:8px;align-items:center}
.tools .login{background:var(--orange);color:#fff;font-size:11px;padding:4px 12px;border-radius:2px}
.tools .search{width:140px;height:24px;border:1px solid var(--line);font-size:11px;color:#999;padding:4px 8px}
.tools .lang{border:1px solid var(--line);font-size:11px;padding:4px 10px}
.contacts{position:absolute;right:95px;top:58px;display:flex;gap:40px}
.contact{display:flex;gap:8px;align-items:center;font-size:12px;white-space:nowrap}
.contact b{color:var(--blue);display:block;font-weight:600}
.contact svg{width:26px;height:26px;flex:none}
.nav{height:37px;background:var(--blue);display:flex;padding-left:95px;align-items:stretch}
.nav a{color:#fff;font-size:12px;padding:0 14px;display:flex;align-items:center;text-decoration:none}
.nav a.active{background:var(--orange)}

/* hero */
.hero{height:515px;position:relative;background:linear-gradient(110deg,#c9ced4 0%,#eef0f2 45%,#b9c1ca 100%)}
.hero-caption{position:absolute;left:95px;top:210px;width:430px}
.hero-caption h1{font-family:"Cinzel",Georgia,serif;font-weight:400;font-size:30px;color:#fff;background:rgba(30,30,30,.55);display:inline-block;padding:6px 14px}
.hero-caption p{background:rgba(30,30,30,.45);color:#ffd49a;font-size:14px;line-height:1.5;padding:8px 14px;margin-top:4px}
.dots{position:absolute;left:0;right:0;bottom:18px;display:flex;justify-content:center;gap:8px}
.dots i{width:10px;height:10px;border-radius:50%;background:#fff;opacity:.6;display:block}
.dots i.on{opacity:1;background:var(--orange)}

/* welcome */
.welcome{height:430px;position:relative}
.welcome .crest{position:absolute;left:95px;top:42px;width:30px;height:30px;border:2px solid var(--navy)}
.welcome h2{position:absolute;left:95px;top:95px;font-family:"Cinzel",Georgia,serif;font-weight:400;font-size:28px;color:#222}
.welcome h2 span{color:var(--blue)}
.welcome .rule{position:absolute;left:95px;top:140px;width:60px;height:2px;background:var(--orange)}
.welcome .copy{position:absolute;left:95px;top:165px;width:760px;font-size:13px;line-height:1.75}
.welcome .copy p{margin-bottom:8px}
.welcome .copy .btn{margin-top:6px}
.pillars{position:absolute;left:910px;top:120px;width:240px}
.pillar{display:flex;gap:14px;margin-bottom:22px}
.pillar svg{width:46px;height:46px;flex:none}
.pillar h3{font-family:"Cinzel",Georgia,serif;color:var(--blue);font-size:16px;font-weight:700}
.pillar p{font-size:11px;color:var(--muted);line-height:1.5}

/* services */
.services{height:525px;background:var(--grey);padding-top:40px}
.svc-grid{display:flex;justify-content:center;gap:36px;margin-top:45px}
.svc{width:230px;text-align:center}
.svc .ring{width:96px;height:96px;border-radius:50%;background:var(--orange);margin:0 auto;display:flex;align-items:center;justify-content:center}
.svc .ring span{width:72px;height:72px;border-radius:50%;background:#fff;display:flex;align-items:center;justify-content:center}
.svc h3{font-family:"Cinzel",Georgia,serif;font-size:15px;font-weight:700;margin:22px 0 8px;color:#222}
.svc p{font-size:12px;color:var(--muted);line-height:1.6;margin-bottom:14px}

/* courses */
.courses{height:1045px;padding-top:40px}
.course-grid{display:grid;grid-template-columns:repeat(3,290px);gap:40px 50px;justify-content:center;margin-top:40px}
.course{text-align:center}
.course .ph{height:190px}
.course h3{font-family:"Cinzel",Georgia,serif;font-size:15px;font-weight:700;margin:22px 0 12px;color:#222;line-height:1.4;min-height:42px}

/* why */
.why{height:745px;background:var(--grey);position:relative;padding-top:40px}
.why .sec-head h2{color:var(--orange)}
.why .sec-head h2 span{color:var(--navy)}
.why-brand{position:absolute;left:110px;top:290px;width:250px;text-align:center}
.why-brand .name{font-weight:700;color:var(--navy);font-size:20px;line-height:1.3}
.why-brand .mark{width:110px;height:110px;background:var(--navy);margin:16px auto 0}
.why-arc{position:absolute;left:330px;top:140px}
.reason{position:absolute;display:flex;gap:16px;width:480px}
.reason .dot{width:64px;height:64px;border-radius:50%;background:var(--navy);flex:none;display:flex;align-items:center;justify-content:center;border:4px solid #fff;box-shadow:0 0 0 1px var(--line)}
.reason h3{color:var(--blue);font-size:15px;font-weight:700;margin-top:6px}
.reason p{font-size:12px;color:#555;line-height:1.5}

/* blog */
.news{height:405px;display:flex;gap:60px;padding:40px 95px 0}
.news h2{font-family:"Cinzel",Georgia,serif;font-size:24px;font-weight:400;color:#222;display:flex;justify-content:space-between;align-items:center}
.news .col{width:475px}
.blog-card{display:flex;gap:16px;margin-top:26px;border:1px solid var(--line);padding:12px;position:relative}
.blog-card .ph{width:190px;height:170px;flex:none}
.blog-card .date{position:absolute;left:400px;top:12px;background:var(--orange);color:#fff;text-align:center;width:48px;padding:4px 0;font-size:11px;line-height:1.2}
.blog-card .date b{font-size:18px;display:block}
.blog-card .txt{padding-top:62px}
.blog-card h4{font-size:13px;margin-bottom:4px}
.blog-card p{font-size:11px;color:var(--muted);line-height:1.5;margin-bottom:8px}
.follow{font-size:11px;border:1px solid var(--line);padding:3px 10px;font-family:"Open Sans",sans-serif;color:var(--blue)}
.tweet{display:flex;gap:12px;border-bottom:1px solid var(--line);padding:12px 0;margin-top:4px}
.tweet .av{width:40px;height:40px;background:#cfd6df;flex:none}
.tweet b{color:var(--blue);font-size:11px}
.tweet p{font-size:11px;color:#666;line-height:1.4;width:330px}
.tweet time{font-size:10px;color:#999;margin-left:auto;white-space:nowrap}

/* candidate */
.split{height:255px;background:linear-gradient(90deg,#151515,#2a2a2a 50%,#151515);position:relative;color:#fff}
.split .side{position:absolute;top:28px;width:400px}
.split h2{font-family:"Cinzel",Georgia,serif;font-size:28px;font-weight:400;display:flex;gap:10px;align-items:center;white-space:nowrap}
.split h4{font-size:12px;margin:14px 0 4px}
.split p{font-size:12px;color:#ccc;line-height:1.5;margin-bottom:12px}
.split .seal{position:absolute;left:505px;top:30px;width:190px;height:190px;border-radius:50%;border:6px solid #fff;background:var(--navy);display:flex;align-items:center;justify-content:center;text-align:center;font-weight:700;font-size:15px;line-height:1.3;padding:20px}

/* promo */
.promo{height:170px;background:var(--orange);display:flex;align-items:center;padding:0 95px;justify-content:space-between}
.promo p{color:#fff;font-size:24px;font-weight:700;line-height:1.4;width:820px}
.promo .book{background:#fff;color:#222;font-weight:700;font-size:14px;padding:12px 22px}

/* testimonials */
.testis{height:420px;padding-top:60px}
.quote-row{display:flex;gap:40px;justify-content:center;margin-top:40px;position:relative}
.quote{width:480px}
.quote blockquote{border:1px solid var(--line);padding:20px 24px;font-size:13px;color:var(--muted);line-height:1.6}
.quote .who{display:flex;align-items:center;gap:14px;margin-top:22px;padding-left:40px}
.quote .who .ph{width:56px;height:56px;border-radius:50%}
.quote .who b{font-family:"Cinzel",Georgia,serif;font-size:14px}
.arrow{position:absolute;top:40px;font-size:22px;color:#bbb}

/* newsletter + footer */
.newsletter{height:70px;background:#111;display:flex;align-items:center;padding:0 130px;gap:14px;color:#fff;font-size:14px}
.newsletter .field{width:260px;height:32px;background:#fff;color:#999;font-size:12px;padding:8px 10px}
.newsletter .sub{background:#fff;color:#111;font-weight:700;padding:7px 16px}
.newsletter .socials{position:static;margin-left:auto}
.newsletter .socials i{background:#555}
.footer{height:285px;background:var(--dark);color:#ccc;display:flex;padding:30px 95px 0;gap:20px}
.footer h4{color:#fff;font-size:17px;font-weight:600;margin-bottom:14px}
.footer ul{list-style:none;font-size:12px;line-height:2.3;white-space:nowrap}
.footer ul li::before{content:"› ";color:var(--orange)}
.quick{width:340px}
.links{display:flex;gap:24px}
.info{width:230px}
.info p{font-size:12px;line-height:1.6;margin-bottom:10px;display:flex;gap:8px}
.form{width:240px}
.form .f{width:240px;height:24px;background:#fff;color:#999;font-size:11px;padding:4px 8px;margin-bottom:6px}
.form .pair{display:flex;gap:6px}
.form .pair .f{width:117px}
.form .msg{height:40px}
.form .btn{background:#fff;color:#111;padding:4px 14px}
.foot-brand{margin-left:auto;text-align:center;width:160px}
.foot-brand .name{font-weight:700;color:#fff;font-size:15px;line-height:1.3}
.foot-brand .mark{width:70px;height:70px;border-radius:50%;background:#3a3a3a;margin:12px auto 0}
.copyright{height:50px;background:#0e0e0e;color:#aaa;font-size:12px;display:flex;align-items:center;justify-content:center}
</style>
</head>
<body>

<header class="topbar">
  <div class="brand"><span class="mark"></span><span class="name">Wellmere Institute of Training</span></div>
  <div class="socials"><i></i><i></i><i></i><i></i><i></i></div>
  <div class="tools">
    <span class="login">Login/Register</span>
    <span class="search">Search</span>
    <span class="lang">English ▾</span>
  </div>
  <div class="contacts">
    <div class="contact">
      <svg viewBox="0 0 26 26"><circle cx="13" cy="13" r="13" fill="#f39a1e"/><path d="M9 7l3 3-1.5 2a9 9 0 0 0 4 4l2-1.5 3 3-2 2c-5 0-10-5-10-10z" fill="#fff"/></svg>
      <div><b>Call Us:</b>+61 (02) 5550 1834</div>
    </div>
    <div class="contact">
      <svg viewBox="0 0 26 26"><circle cx="13" cy="13" r="13" fill="#f39a1e"/><rect x="7" y="9" width="12" height="9" fill="#fff"/><path d="M7 9l6 5 6-5" stroke="#f39a1e" fill="none"/></svg>
      <div><b>Mail Us:</b>hello@wellmere.example</div>
    </div>
  </div>
</header>

<nav class="nav">
  <a class="active">Home</a><a>About Us</a><a>Recruitment</a><a>Courses</a><a>Class Schedule</a><a>Traineeships Queensland Funding</a><a>Latest News Blog</a><a>Corporate Training</a><a>Contact Us</a>
</nav>

<section class="hero" role="img" aria-label="Photo of a presenter in a suit leading a training session with seated professionals">
  <div class="hero-caption">
    <h1>Courses for Busy People</h1>
    <p>Our unique FlexPath (Combined Assessment &amp; Training) class format delivers accelerated training that's specifically targeted at busy professionals...</p>
  </div>
  <div class="dots"><i class="on"></i><i></i><i></i><i></i></div>
</section>

<section class="welcome">
  <span class="crest"></span>
  <h2>Welcome to <span>Wellmere Institute of Training</span></h2>
  <span class="rule"></span>
  <div class="copy">
    <p>Wellmere is Australia's Leading Provider of Educational, Training and Support Services for the Medical and Dental industry – enabling students to be immediately skilled and 'Job Ready' for a career in Health.</p>
    <p>Wellmere is a Registered Training Organisation offering specialised Medical Administration Training in over 15 locations Australia wide. Wellmere have trained thousands of students the required knowledge and skills to become successful health care administrators.</p>
    <p>Our unique Short Medical Reception and Terminology Course and our Full Qualification is Nationally Accredited and the gold recognised qualification in industry.</p>
    <span class="btn">Read More</span>
  </div>
  <div class="pillars">
    <div class="pillar">
      <svg viewBox="0 0 46 46"><circle cx="23" cy="23" r="22" fill="#fff" stroke="#ccc"/><path d="M12 15h10v17H12zM24 15h10v17H24z" fill="none" stroke="#333" stroke-width="2"/></svg>
      <div><h3>Story</h3><p>Wellmere Health Management started business in February 1999 primarily... [+]</p></div>
    </div>
    <div class="pillar">
      <svg viewBox="0 0 46 46"><circle cx="23" cy="23" r="22" fill="#fff" stroke="#ccc"/><path d="M10 23q13-13 26 0q-13 13-26 0z" fill="none" stroke="#333" stroke-width="2"/><circle cx="23" cy="23" r="4" fill="#333"/></svg>
      <div><h3>Vision</h3><p>Wellmere Health Management started business in February 1999 primarily... [+]</p></div>
    </div>
    <div class="pillar">
      <svg viewBox="0 0 46 46"><circle cx="23" cy="23" r="22" fill="#fff" stroke="#ccc"/><path d="M10 22l7-6 6 4 6-4 7 6-9 8h-8z" fill="none" stroke="#333" stroke-width="2"/></svg>
      <div><h3>Core Values</h3><p>Wellmere Health Management started business in February 1999 primarily... [+]</p></div>
    </div>
  </div>
</section>

<section class="services">
  <div class="sec-head"><div class="crest"></div><h2>Our <span>Service</span></h2><div class="rule"></div></div>
  <div class="svc-grid">
    <div class="svc"><div class="ring"><span><svg width="36" height="36" viewBox="0 0 36 36"><rect x="4" y="6" width="28" height="18" fill="none" stroke="#333" stroke-width="2"/><path d="M10 30h16" stroke="#333" stroke-width="2"/></svg></span></div>
      <h3>Training &amp; Assessment</h3><p>Lorem ipsum dolor sit amet, sed diam nonummy nibh euismod tincidunt ut laoreet dolore</p><span class="btn">Read More</span></div>
    <div class="svc"><div class="ring"><span><svg width="36" height="36" viewBox="0 0 36 36"><rect x="6" y="12" width="24" height="16" fill="none" stroke="#333" stroke-width="2"/><path d="M14 12V8h8v4" fill="none" stroke="#333" stroke-width="2"/></svg></span></div>
      <h3>Business &amp; Management</h3><p>Lorem ipsum dolor sit amet, sed diam nonummy nibh euismod tincidunt ut laoreet dolore</p><span class="btn">Read More</span></div>
    <div class="svc"><div class="ring"><span><svg width="36" height="36" viewBox="0 0 36 36"><path d="M8 18a10 10 0 0 1 20 0z" fill="#f39a1e"/><rect x="6" y="18" width="24" height="3" fill="#333"/></svg></span></div>
      <h3>Work Health &amp; Safety</h3><p>Lorem ipsum dolor sit amet, sed diam nonummy nibh euismod tincidunt ut laoreet dolore</p><span class="btn">Read More</span></div>
    <div class="svc"><div class="ring"><span><svg width="36" height="36" viewBox="0 0 36 36"><rect x="9" y="6" width="18" height="24" fill="none" stroke="#333" stroke-width="2"/><path d="M13 18l4 4 6-8" fill="none" stroke="#f39a1e" stroke-width="2"/></svg></span></div>
      <h3>Project Management</h3><p>Lorem ipsum dolor sit amet, sed diam nonummy nibh euismod tincidunt ut laoreet dolore</p><span class="btn">Read More</span></div>
  </div>
</section>

<section class="courses">
  <div class="sec-head"><div class="crest"></div><h2>Our <span>Courses</span></h2><div class="rule"></div></div>
  <div class="course-grid">
    <div class="course"><div class="ph" role="img" aria-label="Photo of a medical receptionist helping a patient at a desk" style="background:linear-gradient(135deg,#c8b7a2,#e9e4dc)"></div><h3>Medical Reception<br>&amp; Terminology</h3><span class="btn">Read More</span></div>
    <div class="course"><div class="ph" role="img" aria-label="Photo of a smiling business team in office wear" style="background:linear-gradient(135deg,#d9dfe7,#9aa8bb)"></div><h3>Cert III Business<br>Administration</h3><span class="btn">Read More</span></div>
    <div class="course"><div class="ph" role="img" aria-label="Photo of a stethoscope resting on paperwork" style="background:linear-gradient(135deg,#eef1f4,#a9b4bf)"></div><h3>Medical<br>Terminology</h3><span class="btn">Read More</span></div>
    <div class="course"><div class="ph" role="img" aria-label="Photo of hands typing on a keyboard" style="background:linear-gradient(135deg,#8aa6c8,#dfe8f2)"></div><h3>Keyboard<br>and Typing</h3><span class="btn">Read More</span></div>
    <div class="course"><div class="ph" role="img" aria-label="Illustration of a computer mouse beside an online sign" style="background:linear-gradient(135deg,#f4f6f9,#5d8fd0)"></div><h3>Wellmere Online</h3><span class="btn">Read More</span></div>
    <div class="course"><div class="ph" role="img" aria-label="Photo of a confidential stamp on a document folder" style="background:linear-gradient(135deg,#c79a6a,#e8d2b4)"></div><h3>Confidentiality</h3><span class="btn">Read More</span></div>
  </div>
</section>

<section class="why">
  <div class="sec-head"><div class="crest"></div><h2>Why Choose <span>Us</span></h2></div>
  <div class="why-brand"><div class="name">Wellmere Institute<br>of Training</div><div class="mark"></div></div>
  <svg class="why-arc" width="200" height="560" viewBox="0 0 200 560"><path d="M20 10 A290 290 0 0 1 20 550" fill="none" stroke="#b5b5b5" stroke-width="3"/></svg>
  <div class="reason" style="left:440px;top:150px"><span class="dot"><svg width="26" height="26"><circle cx="13" cy="13" r="9" fill="none" stroke="#fff" stroke-width="2"/></svg></span><div><h3>Quality</h3><p>Wellmere delivers quality, effective training facilitated by industry leaders. Just ask our students who rate us on average of 4.7 out of 5.</p></div></div>
  <div class="reason" style="left:520px;top:260px"><span class="dot"><svg width="26" height="26"><path d="M6 20V6h6l2 3h6v11z" fill="#fff"/></svg></span><div><h3>Experience</h3><p>Wellmere is Australia's largest and leading providers of nationally recognised training in health administration – training from over 17 locations Australia wide.</p></div></div>
  <div class="reason" style="left:545px;top:380px"><span class="dot"><svg width="26" height="26"><path d="M5 20h4v-6H5zM11 20h4V9h-4zM17 20h4V4h-4z" fill="#fff"/></svg></span><div><h3>Value</h3><p>Our innovative teaching approach allows us to deliver exceptional training at affordable prices with no hidden extras.</p></div></div>
  <div class="reason" style="left:520px;top:500px"><span class="dot"><svg width="26" height="26"><circle cx="9" cy="11" r="5" fill="#fff"/><circle cx="18" cy="17" r="4" fill="#fff"/></svg></span><div><h3>Industry Recognised</h3><p>Wellmere work hand in hand with industry to develop our core programme and consolidate the programme annually to keep the programme fresh and relevant.</p></div></div>
  <div class="reason" style="left:440px;top:610px"><span class="dot"><svg width="26" height="26"><rect x="7" y="4" width="12" height="18" fill="#fff"/></svg></span><div><h3>Great Job Results</h3><p>Wellmere students get jobs! Our focus is to create job-ready students who are mentored to achieve their goals. Wellmere also provide a recruitment service for industry and graduates.</p></div></div>
</section>

<section class="news">
  <div class="col">
    <h2>Latest Blog <span style="font-size:16px;color:#555">‹ ›</span></h2>
    <div class="blog-card">
      <div class="ph" role="img" aria-label="Photo of a businessman in a suit and tie" style="background:linear-gradient(135deg,#d7dde5,#8a97a8)"></div>
      <div class="date"><b>26</b>June</div>
      <div class="txt"><h4>Lorem ipsum do sit amet,</h4><p>Lorem ipsum dolor sit amet, consectetur adipiscing elit, sed do eiusmod tempor incididunt ut labore et dolore magna aliqua. Ut enim ad minim veniam.</p><span class="btn">Read More</span></div>
    </div>
  </div>
  <div class="col">
    <h2>Latest Tweets <span class="follow">Follow</span></h2>
    <div class="tweet"><span class="av"></span><div><b>Wellmere @wellmere</b><p>Lorem ipsum dolor sit amet, consectetur adipiscing elit, sed diam nonummy nibh euismod tincidunt ut laoreet dolore.</p></div><time>20 mins</time></div>
    <div class="tweet"><span class="av"></span><div><b>Wellmere @wellmere</b><p>Lorem ipsum dolor sit amet, consectetur adipiscing elit, sed diam nonummy nibh euismod tincidunt ut laoreet dolore.</p></div><time>20 mins</time></div>
    <div class="tweet"><span class="av"></span><div><b>Wellmere @wellmere</b><p>Lorem ipsum dolor sit amet, consectetur adipiscing elit, sed diam nonummy nibh euismod tincidunt ut laoreet dolore.</p></div><time>20 mins</time></div>
  </div>
</section>

<section class="split">
  <div class="side" style="left:95px">
    <h2><svg width="24" height="24"><circle cx="12" cy="7" r="5" fill="#fff"/><path d="M2 24a10 10 0 0 1 20 0z" fill="#fff"/></svg>For the Candidate</h2>
    <h4>Looking for a Career in Medical Administration?</h4>
    <p>Our partner company, Wellmere Institute of Training has been the market leader in Medical Reception Training in Australia for over 17 years. In fact, we pioneered.</p>
    <span class="btn">Read More</span>
  </div>
  <div class="seal">Wellmere Institute of Training</div>
  <div class="side" style="left:735px">
    <h2><svg width="24" height="24"><circle cx="12" cy="7" r="5" fill="#fff"/><path d="M2 24a10 10 0 0 1 20 0z" fill="#fff"/></svg>For the Employer</h2>
    <p style="margin-top:14px">Wellmere Recruitment is a leading National Health Specialist Recruitment Agency with expertise in Medical and Dental administration recruitment for both permanent and temporary staff.</p>
    <span class="btn">Read More</span>
  </div>
</section>

<section class="promo">
  <p>Enrol In Our BSB51915 Diploma Of Leadership And Management And Gain Valuable Skills To Launch Your Management Career.</p>
  <span class="book">Booking Now</span>
</section>

<section class="testis">
  <div class="sec-head"><h2>Client <span>Testimonials</span></h2><div class="rule"></div></div>
  <div class="quote-row">
    <span class="arrow" style="left:70px">‹</span>
    <div class="quote"><blockquote>Sam nonummy nibh euismod tincidunt ut laoreet do magna aliquam erat volutpat. Ut wisi enim ad minim veniam, vullum dolore eu feugiat nulla facilisis at vero eros et accumsan et iusto odio dig.</blockquote>
      <div class="who"><span class="ph" role="img" aria-label="Portrait photo of a client" style="background:#c9b8a8"></span><b>Anna Pryce</b></div></div>
    <div class="quote"><blockquote>Sam nonummy nibh euismod tincidunt ut laoreet do magna aliquam erat volutpat. Ut wisi enim ad minim veniam, vullum dolore eu feugiat nulla facilisis at vero eros et accumsan et iusto odio dig.</blockquote>
      <div class="who"><span class="ph" role="img" aria-label="Portrait photo of a client" style="background:#a9a39c"></span><b>Daniel Marsh</b></div></div>
    <span class="arrow" style="right:70px">›</span>
  </div>
</section>

<section class="newsletter">
  <span>Stay updated with latest news from</span>
  <span class="field">Enter Your Email</span>
  <span class="sub">Subscribe</span>
  <div class="socials"><i></i><i></i><i></i><i></i><i></i></div>
</section>

<footer class="footer">
  <div class="quick">
    <h4>Quick Link</h4>
    <div class="links">
      <ul><li>Home</li><li>About Us</li><li>Courses</li><li>Recruitment</li><li>Class Schedule</li><li>Traineeships Queensland Funding</li></ul>
      <ul><li>Latest News Blog</li><li>Corporate Training</li><li>Contact Us</li></ul>
    </div>
  </div>
  <div class="info">
    <h4>Information</h4>
    <p>⌂ <span>Wellmere Health Trainings<br>12 Harbour Lane, Suite 4<br>Brisbane QLD 4000</span></p>
    <p>✆ <span>+61 (02) 5550 1834</span></p>
    <p>✉ <span>hello@wellmere.example</span></p>
  </div>
  <div class="form">
    <h4>Info Pak</h4>
    <div class="f">Name</div>
    <div class="f">Email</div>
    <div class="pair"><div class="f">Course ▾</div><div class="f">State ▾</div></div>
    <div class="f msg">Message</div>
    <span class="btn">Submit</span>
  </div>
  <div class="foot-brand"><div class="name">Wellmere Institute of Training</div><div class="mark"></div></div>
</footer>

<div class="copyright">© 2016 Wellmere Health Trainings. All Right Reserved</div>

</body>
</html>
```